Letterhead Design for Law Firm

**Edit: I have added the photo of a bottom that I like.

------
We are looking for a re-design of our new letterhead. The letterhead is for a law firm and will be used for digital and traditionally printed correspondence.

Here are some suggestions:

- Please use colours are #8ec900 and simple black.
- Please do not use any type of "waves" at the bottom of the page. This is not in style at all.
- Please stay modern yet conservative.
- Please use font Segoe UI Light or similar if you can
- Avoid clipart or illustrations.
- Utilize ample white space in the layout so the design looks clean and information is easy to read at a glance. Don't overcrowd the letterhead.
- Make sure the letterhead design is consistent with our brand identity (see brambleford.ca)
-Please, no black headers or footers.

I am attaching my current letterhead and signature for your convenience.

Remember, the letterhead is an extension of our professional identity. We are a successful firm and trial lawyers who correspond with insurers, judges, lawyers, courts, clients, etc. Make it new, modern, attractive, yet powerful and conservative.

It needs to be easily printable. I would like the bleed removed in print so the black bar the bottom crosses the page (but the text is not near the edges)

Target Market(s)

Clients, Government Offices, Judiciary, Lawyers, Insurance Companies, Colleagues.

Industry/Entity Type

Law

Font styles to use
Other font styles liked:
• Segoe UI LIght, Calibri Light,

Colors
00AB8E
00BBA5
67D7C9
C6EFE9
E9F9F6

Requirements
Must have
• Everything that is on the letterhead now.
Nice to have
• Cutting Edge design, yet conservative.
Should not have
• law firm cliche design, images,

```html
<!DOCTYPE html>
<html lang="en">
<head>
<meta charset="utf-8">
<title>Harrowgate Personal Injury Lawyers – Letterhead</title>
<link rel="stylesheet" href="https://fonts.googleapis.com/css2?family=Open+Sans:wght@300;400;600;700&display=swap">
<style>
  :root {
    --brand-green: #8ec900;
    --ink: #111111;
    --paper: #ffffff;
    --backdrop: #c9c9c9;
    --corner-black: #050708;
  }
  * { box-sizing: border-box; margin: 0; padding: 0; }
  html, body {
    width: 1200px; height: 686px; overflow: hidden;
    background: radial-gradient(ellipse at center, #e6e6e6 0%, var(--backdrop) 75%);
    font-family: "Open Sans", "Segoe UI", sans-serif;
    color: var(--ink);
  }
  .letterhead {
    position: absolute; left: 350px; top: 20px;
    width: 500px; height: 647px;
    background: var(--paper);
    box-shadow: 0 6px 18px rgba(0,0,0,.18);
    overflow: hidden;
  }
  .frame { position: absolute; inset: 0; }
  .wordmark {
    position: absolute; left: 52px; top: 22px;
    font-weight: 300; color: var(--ink);
  }
  .wordmark-name { font-size: 30px; letter-spacing: 1px; line-height: 1; }
  .wordmark-tagline {
    font-size: 7.5px; letter-spacing: 1.6px; margin-top: 4px;
    padding-top: 3px; border-top: 1px solid var(--brand-green);
  }
  .correspondence {
    position: absolute; left: 52px; top: 84px;
    font-size: 8px; line-height: 11px;
  }
  .correspondence .strong { font-weight: 700; }
  .correspondence .gap { margin-top: 9px; }
  .recipient { margin-top: 9px; }
  .reference { display: flex; margin-top: 9px; }
  .reference-label { width: 60px; }
  .reference-lines { font-weight: 700; }
  .header-rule {
    position: absolute; left: 40px; top: 300px;
    width: 352px; height: 1px; background: var(--brand-green);
  }
  .contact {
    position: absolute; left: 358px; top: 178px;
    padding-left: 8px; border-left: 1px solid var(--brand-green);
    font-size: 7.2px; line-height: 10px;
  }
  .contact-web { color: var(--brand-green); }
  .practice { margin-top: 8px; }
  .sign-off {
    position: absolute; right: 30px; top: 478px;
    text-align: right; font-size: 8px; line-height: 11px;
  }
  .sign-off .firm { font-weight: 600; }
  .signature {
    display: block; margin: 6px 0 4px auto;
    width: 170px; height: 44px;
  }
  .sign-off .corp { font-weight: 700; }
</style>
</head>
<body>
<main class="letterhead">
  <svg class="frame" viewBox="0 0 500 647" width="500" height="647" aria-hidden="true">
    <polygon points="0,0 22,0 22,536 106,647 84,647 0,534" fill="var(--brand-green)"/>
    <polygon points="0,534 0,647 84,647" fill="var(--corner-black)"/>
    <polygon points="424,0 500,0 500,58" fill="var(--corner-black)"/>
  </svg>

  <header class="wordmark">
    <div class="wordmark-name">HARROWGATE</div>
    <div class="wordmark-tagline">PERSONAL INJURY LAWYERS</div>
  </header>

  <section class="correspondence">
    <p class="strong">Without Prejudice</p>
    <p class="gap">March 13, 2024</p>
    <p class="gap strong">By Email</p>
    <address class="recipient" style="font-style:normal">
      Corvale Insurance Company<br>
      Claims Litigation Department<br>
      48 Fernhill Road North<br>
      P.O. Box 410<br>
      Waterloo, ON&nbsp; N2K 3B7
    </address>
    <p class="gap">Attention:&nbsp; Mr. Dorian Vale</p>
    <p class="gap">Mr. Vale:</p>
    <div class="reference">
      <span class="reference-label">Re:</span>
      <div class="reference-lines">
        Marsh v. Ketteridge et al.<br>
        DOL: September 12, 2019<br>
        Pre-Mediation Settlement Proposal – March 13th, 2024
      </div>
    </div>
  </section>

  <div class="header-rule"></div>

  <aside class="contact">
    <p class="contact-web">www.brambleford.ca</p>
    <p>27 Ashgrove Avenue, Suite 904</p>
    <p>Hamilton, ON L8R 2C6</p>
    <p>T: 905-555-0142</p>
    <p>F: 905-555-0187</p>
    <p>File Clerk: Nadia Pellew</p>
    <p>Email: nadia@brambleford.ca</p>
    <div class="practice">
      <p>Practice Restricted</p>
      <p>Serious Personal Injury</p>
      <p>Wrongful Death Litigation</p>
      <p>Long-Term Disability Litigation</p>
      <p>Wrongful Dismissal Litigation</p>
      <p>Employee Terminations</p>
    </div>
  </aside>

  <footer class="sign-off">
    <p>Yours very truly,</p>
    <p class="firm">HARROWGATE PERSONAL INJURY LAWYERS</p>
    <svg class="signature" viewBox="0 0 170 44" role="img" aria-label="Handwritten signature of Owen T. Harrowgate">
      <rect width="170" height="44" fill="#ececec"/>
    </svg>
    <p>Owen T. Harrowgate</p>
    <p class="corp">Harrowgate Law Professional Corporation</p>
    <p>/np</p>
    <p>Encl.</p>
  </footer>
</main>
</body>
</html>
```